Brickline Kit - iPhone app for tradespeople - UI design

Brickline Kit is an iPhone app for tradespeople (builders, carpenters, electricians, etc) which provides a range of tools that will assist with typical tasks, such as the calculation of unit conversion and spatial/volumetric/electrical measurements. The application also makes use of instruments available in the smartphone device to provide useful tools such as a spirit level, compass and torch.

The product is a simple menu-based application consisting of a number of menu and function screens. Each menu item will navigate the user to the function screen applicable to that menu item. Each function screen will contain the necessary inputs and features for perform its stated function.

The user interface should be designed with the tradesperson user in mind and as such should be simple, intuitive and durable with respect to its usability, interface design and branding elements.

Target Market(s)

Tradespeople (builders, carpenters, electricians, etc)

Industry/Entity Type

Trade

Font styles to use
Sans Serif

Requirements
Must have
• Refer to attached wireframes document...
• - Simple design
• - Consistent layout and theme
• - Screens and icons
Should not have
• - Tacky 3D images and textured backgrounds

```html
<!DOCTYPE html>
<html lang="en">
<head>
<meta charset="utf-8">
<title>Brickline Kit – App Screens</title>
<link rel="stylesheet" href="https://fonts.googleapis.com/css2?family=Barlow+Semi+Condensed:wght@400;500&display=swap">
<style>
  :root {
    --stage: #2a2a2a;
    --ink-black: #121212;
    --orange: #f39c12;
    --orange-deep: #e8920f;
    --light-panel: #f2f2f2;
    --light-rule: #dcdcdc;
    --text-dark: #2b2b2b;
    --muted: #8a8a8a;
  }
  * { box-sizing: border-box; margin: 0; padding: 0; }
  html, body {
    width: 1200px; height: 745px; overflow: hidden;
    background: var(--stage);
    font-family: "Barlow Semi Condensed", "Arial Narrow", sans-serif;
  }
  .canvas { position: relative; width: 1200px; height: 745px; }

  .screen {
    position: absolute; top: 105px;
    width: 300px; height: 534px; overflow: hidden;
    background: var(--ink-black);
  }
  .screen--splash { left: 51px; }
  .screen--menu { left: 449px; }
  .screen--contact { left: 848px; background: var(--light-panel); }

  .backdrop {
    position: absolute; inset: 0;
    background:
      radial-gradient(ellipse at 30% 20%, rgba(90,90,90,.45), transparent 60%),
      radial-gradient(ellipse at 75% 70%, rgba(70,70,70,.4), transparent 55%),
      linear-gradient(160deg, #1f1f1f, #141414 55%, #1c1c1c);
  }

  .status-bar {
    position: absolute; top: 0; left: 0; right: 0; height: 20px;
    display: flex; align-items: center; justify-content: space-between;
    padding: 0 8px; font-size: 9px; color: var(--orange);
    background: #0d0d0d; z-index: 2;
  }
  .status-bar__time { position: absolute; left: 0; right: 0; text-align: center; }
  .status-bar__right { display: flex; align-items: center; gap: 4px; }

  .wordmark {
    color: var(--orange); font-weight: 400; letter-spacing: .5px;
    text-transform: uppercase; white-space: nowrap;
  }

  /* Splash */
  .splash__mark {
    position: absolute; left: 0; right: 0; top: 228px;
    text-align: center; font-size: 31px; z-index: 1;
  }
  .splash__legal {
    position: absolute; left: 20px; right: 20px; bottom: 20px;
    text-align: center; font-size: 5.5px; line-height: 7px;
    color: #5a5a5a; text-transform: uppercase; z-index: 1;
  }

  /* Header */
  .app-header {
    position: absolute; top: 20px; left: 0; right: 0; height: 66px;
    background: var(--ink-black); border-bottom: 1px solid var(--orange-deep);
    display: flex; align-items: center; justify-content: center; z-index: 1;
  }
  .app-header .wordmark { font-size: 24px; }
  .app-header__mail { position: absolute; right: 18px; top: 26px; }
  .app-header__back { position: absolute; left: 16px; top: 24px; }
  .app-header__title { color: var(--orange); font-size: 21px; letter-spacing: .5px; }

  /* Menu */
  .menu__intro {
    position: absolute; top: 120px; left: 0; right: 0;
    display: flex; flex-direction: column; align-items: center; gap: 12px; z-index: 1;
  }
  .menu__prompt { color: var(--orange); font-size: 12.5px; letter-spacing: .3px; }
  .menu__list {
    position: absolute; top: 223px; left: 28px; width: 245px;
    list-style: none; display: flex; flex-direction: column; gap: 7px; z-index: 1;
  }
  .menu__item {
    height: 49px; border: 1px solid #8a5c12;
    display: flex; align-items: center; justify-content: center;
    color: var(--orange); font-size: 15px; background: rgba(10,10,10,.35);
  }
  .menu__footer-bar {
    position: absolute; left: 0; right: 0; bottom: 0; height: 5px;
    background: var(--orange); z-index: 1;
  }

  /* Contact */
  .contact__body {
    position: absolute; top: 86px; left: 0; right: 0; bottom: 0;
    border: 1px solid var(--light-rule); border-top: none;
  }
  .contact__mark {
    position: absolute; top: 54px; left: 0; right: 0;
    text-align: center; font-size: 24px;
  }
  .contact__message {
    position: absolute; top: 92px; left: 20px; right: 20px;
    text-align: center; font-size: 14px; line-height: 20px; color: var(--text-dark);
  }
  .contact__actions {
    position: absolute; top: 184px; left: 28px; width: 245px;
    display: flex; flex-direction: column; gap: 8px;
  }
  .contact__button {
    height: 48px; background: var(--orange); color: #fff;
    display: flex; align-items: center; justify-content: center; font-size: 15px;
  }
  .contact__credit {
    position: absolute; bottom: 22px; left: 10px; right: 10px;
    text-align: center; font-size: 9.5px; line-height: 13px; color: var(--text-dark);
  }
</style>
</head>
<body>
<main class="canvas">

  <!-- Splash screen -->
  <section class="screen screen--splash">
    <div class="backdrop" role="img" aria-label="Blurred dark photo of a workshop tool wall"></div>
    <div class="status-bar">
      <span>●●●○○ 3</span><span class="status-bar__time">16:05</span>
      <span class="status-bar__right">67%
        <svg width="18" height="8" viewBox="0 0 18 8"><rect x=".5" y=".5" width="15" height="7" rx="1.5" fill="none" stroke="#f39c12"/><rect x="2" y="2" width="9" height="4" fill="#f39c12"/><rect x="16" y="2.5" width="1.5" height="3" fill="#f39c12"/></svg>
      </span>
    </div>
    <div class="splash__mark wordmark">Brickline Kit</div>
    <p class="splash__legal">© 2015 Brickline Kit<br>Practical tools for builders, carpenters and electricians. Measure, convert, level<br>and find your way on every site, day or night.</p>
  </section>

  <!-- Menu screen -->
  <section class="screen screen--menu">
    <div class="backdrop" role="img" aria-label="Blurred dark photo of a workshop tool wall"></div>
    <div class="status-bar">
      <span>●●●○○ 3</span><span class="status-bar__time">16:05</span>
      <span class="status-bar__right">67%
        <svg width="18" height="8" viewBox="0 0 18 8"><rect x=".5" y=".5" width="15" height="7" rx="1.5" fill="none" stroke="#f39c12"/><rect x="2" y="2" width="9" height="4" fill="#f39c12"/><rect x="16" y="2.5" width="1.5" height="3" fill="#f39c12"/></svg>
      </span>
    </div>
    <header class="app-header">
      <span class="wordmark">Brickline Kit</span>
      <svg class="app-header__mail" width="15" height="11" viewBox="0 0 15 11" aria-label="Contact"><rect x=".75" y=".75" width="13.5" height="9.5" fill="none" stroke="#f39c12" stroke-width="1.5"/><path d="M1 1l6.5 5L14 1" fill="none" stroke="#f39c12" stroke-width="1.5"/></svg>
    </header>
    <div class="menu__intro">
      <svg width="50" height="40" viewBox="0 0 50 40" aria-hidden="true">
        <path d="M17 8V3h16v5" fill="none" stroke="#f39c12" stroke-width="3"/>
        <rect x="1" y="8" width="48" height="31" rx="2" fill="#f39c12"/>
        <rect x="1" y="19" width="48" height="2" fill="#121212"/>
        <rect x="21" y="16" width="8" height="8" fill="#f39c12" stroke="#121212" stroke-width="2"/>
      </svg>
      <p class="menu__prompt">CHOOSE YOUR WORKING TOOLS</p>
    </div>
    <ul class="menu__list">
      <li class="menu__item">Unit Conversion</li>
      <li class="menu__item">Measurement Calculation</li>
      <li class="menu__item">Spirit Level</li>
      <li class="menu__item">Compass</li>
      <li class="menu__item">Torch</li>
    </ul>
    <div class="menu__footer-bar"></div>
  </section>

  <!-- Contact screen -->
  <section class="screen screen--contact">
    <div class="status-bar">
      <span>●●●○○ 3</span><span class="status-bar__time">16:05</span>
      <span class="status-bar__right">67%
        <svg width="18" height="8" viewBox="0 0 18 8"><rect x=".5" y=".5" width="15" height="7" rx="1.5" fill="none" stroke="#f39c12"/><rect x="2" y="2" width="9" height="4" fill="#f39c12"/><rect x="16" y="2.5" width="1.5" height="3" fill="#f39c12"/></svg>
      </span>
    </div>
    <header class="app-header">
      <svg class="app-header__back" width="20" height="16" viewBox="0 0 20 16" aria-label="Back"><path d="M19 8H2M8 1.5L1.5 8 8 14.5" fill="none" stroke="#f39c12" stroke-width="1.8"/></svg>
      <h1 class="app-header__title">CONTACT US</h1>
    </header>
    <div class="contact__body">
      <div class="contact__mark wordmark">Brickline Kit</div>
      <p class="contact__message">For feedback and suggestions,<br>please visit our website. Dont forget to<br>rate our apps.</p>
      <div class="contact__actions">
        <div class="contact__button">Visit website</div>
        <div class="contact__button">Rate us</div>
      </div>
      <p class="contact__credit">Brickline Kit is brought to you by Norvale Digital Works<br>(c) 2015. All rights reserved.</p>
    </div>
  </section>

</main>
</body>
</html>
```